Webdesign für Online-Börse für Porzellan, Gläser und Besteck
Zielgruppe
Wir sind eine Online-Börse für Porzellan, Gläser und Besteck. Auf www.tassenfund.de verkaufen wir gebrauchte Artikel von renommierten Herstellern. Unser Sortiment umfasst 100.000 verschiedene Artikel - die meisten davon sind nicht mehr als Neuware erhältlich (alte, ausgelaufene Serien). Zusätzlich zur Gebrauchtware verkaufen wir auch etwas Neuware über den Shop.
Zudem bieten wir auch den Ankauf von gebrauchtem Porzellan an.
Unsere Zielgruppe sind Besitzer von Porzellan, größtenteils 50+ Jahre alt, die ihre bestehenden Serien ergänzen oder erweitern wollen und die Artikel nicht mehr als Neuware kaufen können. In erster Linie gezieltes Ersatzteilgeschäft.
Zudem gibt es einen Anteil an Stöberkunden und Liebhabern, die sich durch Kategorien, Inspiration oder Rabattstufen klicken.
Aufgabenstellung
Zielsetzung ist das Redesign des bestehenden Webshops tassenfund.de
- Mehr Emotionen transportieren (z.B. über Bilder)
- Zielgruppe: 50+ ansprechen (nicht zu modern; soll weiterhin zur Brand “tassenfund.de” passen)
- Fokus auf Mobile Version (Mobile + Desktop Version Benötigt)
- Verwenden des Ziel-CIs (siehe Dateiupload für Farben und Schriften)
(Abweichungen von den Farben, Schriften möglich, wenn aus Designsicht/Farbensicht sinnvoll)
- Neue Teaser mit Bildern
- Benefits für den Kunden auf den Seiten einbauen (Startseite, Collection, PDS, ggf. in Produkt-Bilder), z.B.:
1) Finden Sie Ihre ausgelaufenen Schätze und Serien
2) von Experten geprüfte Originalware
3) Qualitätsgarantie für unsere Zustände
4) garantierte bruchsichere Lieferung
- Social Proof Element einbauen (Kundenbewertungen)
- CTA Buttons mit positivem Wording
- möglichst keine/wenig Slider
- In Figma erstellen, wenn möglich
- Verwenden des Hero Teasers auf Startseite (siehe Anhang - wir haben neben dem aktuell verwendeten auch noch eines mit weißem Hintergund hinzugepackt, falls das neue Design eine andere Hintergrundfarbe nehmen soll)

```html
<!DOCTYPE html>
<html lang="de">
<head>
<meta charset="utf-8">
<title>Tassenfund – Mobile Webdesign</title>
<link href="https://fonts.googleapis.com/css2?family=Libre+Baskerville:wght@700&family=Roboto:wght@400;500;700&display=swap" rel="stylesheet">
<style>
:root{
  --navy:#0c2a5b;
  --navy-soft:#4a6290;
  --bg:#ffffff;
  --screen:#eef2f8;
  --card:#ffffff;
  --orange:#f26b3a;
  --text:#0c2a5b;
  --muted:#8a97ad;
  --img-blue:linear-gradient(135deg,#dfe7f4 0%,#9fb3d8 45%,#3f62a8 100%);
  --img-paper:linear-gradient(135deg,#d9cbb4 0%,#b8a07e 60%,#8f7456 100%);
  --img-plates:linear-gradient(135deg,#c9b79b 0%,#4b6aa6 50%,#1c3b7a 100%);
  --img-plate:radial-gradient(circle,#fbf7f2 0%,#f3e6dc 55%,#9cb58e 70%,#f6efe8 78%);
  --img-bowl:radial-gradient(ellipse at 50% 40%,#ffffff 0%,#e7edf7 45%,#8ea5d3 75%,#dfe6f3 100%);
}
*{box-sizing:border-box;margin:0;padding:0}
html,body{width:1200px;height:642px;overflow:hidden;background:var(--bg)}
body{font-family:"Roboto",sans-serif;color:var(--text)}
.canvas{position:relative;width:1200px;height:642px;overflow:hidden}
.stage{position:absolute;left:0;top:0;width:1860px;height:995px;transform:scale(.64516);transform-origin:0 0}
.abs{position:absolute}
.screen{position:absolute;background:var(--screen);overflow:hidden}
.serif{font-family:"Libre Baskerville",serif;font-weight:700}
.label{position:absolute;font-size:14px;font-weight:700;color:#111;transform:translateX(-50%);white-space:nowrap}
.logo{position:absolute;left:14px;top:12px;display:flex;align-items:center;gap:6px;font-family:"Libre Baskerville",serif;font-weight:700;font-size:12px;color:var(--navy)}
.logo i{width:12px;height:12px;border-radius:50%;background:var(--navy-soft);display:block}
.burger{position:absolute;right:12px;top:16px;width:12px;height:8px;border-top:1.5px solid var(--navy);border-bottom:1.5px solid var(--navy)}
.burger::after{content:"";position:absolute;left:0;right:0;top:2.5px;border-top:1.5px solid var(--navy)}
.h2{position:absolute;font-family:"Libre Baskerville",serif;font-weight:700;font-size:18px;line-height:1.15;color:var(--navy);white-space:nowrap}
.btn{position:absolute;display:flex;align-items:center;justify-content:center;border-radius:14px;font-size:8px;font-weight:500;color:#fff;background:var(--orange);white-space:nowrap}
.btn.navy{background:var(--navy-soft)}
.btn.outline{background:transparent;border:1.5px solid var(--navy);color:var(--navy);font-size:7px}
.link{position:absolute;font-size:7px;color:var(--navy);text-decoration:underline;white-space:nowrap}
.img{position:absolute}
.card{position:absolute;background:var(--card);border-radius:8px;overflow:hidden}
.pcard .name{position:absolute;font-family:"Libre Baskerville",serif;font-weight:700;font-size:10px;line-height:1.15;white-space:nowrap}
.pcard .meta{position:absolute;font-size:6px;color:var(--muted);white-space:nowrap}
.pcard .price{position:absolute;font-size:13px;font-weight:500;white-space:nowrap}
.plate{position:absolute;border-radius:50%;background:var(--img-plate)}
.tag{position:absolute;width:22px;height:20px;border-radius:0 0 0 6px;display:flex;align-items:center;justify-content:center}
.tag svg{width:9px;height:9px}
.chips{position:absolute;display:flex;flex-wrap:wrap;gap:5px 4px}
.chip{height:18px;padding:0 8px;border-radius:9px;background:var(--navy);color:#fff;font-size:7.5px;font-weight:500;display:flex;align-items:center;white-space:nowrap}
.chip.out{background:#fff;color:var(--navy);border:1px solid var(--navy)}
.para{position:absolute;font-size:8px;line-height:1.6;color:var(--muted)}
.cat{position:absolute;left:12px;width:211px;height:30px;background:#fff;border-radius:5px;display:flex;align-items:center;gap:14px;padding-left:14px;font-family:"Libre Baskerville",serif;font-weight:700;font-size:8px}
.cat svg{width:13px;height:11px}
.foot{position:absolute;left:16px;font-size:11px;color:#fff;white-space:nowrap}
.glass{position:absolute;background:rgba(238,242,248,.82);border-radius:8px}
.cond{display:flex;gap:4px;position:absolute}
.cond span{height:17px;padding:0 8px;border-radius:9px;border:1px solid var(--navy);font-size:7px;display:flex;align-items:center;white-space:nowrap}
.cond span.on{background:var(--navy);color:#fff}
</style>
</head>
<body>
<svg width="0" height="0" style="position:absolute">
  <defs>
    <symbol id="bag" viewBox="0 0 10 10"><rect x="1.5" y="3" width="7" height="6" rx="1" fill="none" stroke="#fff" stroke-width="1.2"/><path d="M3.5 3V2a1.5 1.5 0 013 0v1" fill="none" stroke="#fff" stroke-width="1.2"/></symbol>
    <symbol id="cup" viewBox="0 0 13 11"><rect x="1" y="1" width="11" height="7" rx="1.5" fill="none" stroke="#0c2a5b" stroke-width="1.4"/><path d="M4 10h5" stroke="#0c2a5b" stroke-width="1.4"/></symbol>
    <symbol id="heart" viewBox="0 0 12 11"><path d="M6 10L1.5 5.6A2.8 2.8 0 016 1.9a2.8 2.8 0 014.5 3.7z" fill="none" stroke="#0c2a5b" stroke-width="1.2"/></symbol>
  </defs>
</svg>

<div class="canvas">
<div class="stage">

  <!-- Startseite -->
  <div class="label" style="left:223px;top:71px">Startseite</div>
  <div class="screen" style="left:105px;top:115px;width:235px;height:880px;border-radius:14px 14px 0 0">
    <div class="img" role="img" aria-label="Blaues Porzellangeschirr von oben fotografiert" style="left:0;top:0;width:235px;height:282px;background:var(--img-blue)"></div>
    <div class="logo"><i></i>Tassenfund</div><div class="burger"></div>
    <div class="glass" style="left:25px;top:80px;width:202px;height:95px"></div>
    <div class="abs serif" style="left:25px;top:98px;font-size:21px">Porzellanbörse</div>
    <div class="abs serif" style="left:25px;top:126px;font-size:12px;line-height:1.3">für Porzellan, Glaswaren<br>und Besteck</div>
    <div class="btn" style="left:25px;top:182px;width:108px;height:25px">Jetzt verkaufen</div>
    <div class="h2" style="left:11px;top:309px">Neu eingetroffene<br>Produkte</div>
    <div class="card pcard" style="left:11px;top:370px;width:213px;height:85px">
      <div class="name" style="left:12px;top:11px">Kuchenteller<br>altes Modell</div>
      <div class="meta" style="left:12px;top:38px">Lindhorst &amp; Sohn Heckenrose</div>
      <div class="price" style="left:12px;top:57px">€ 4,57</div>
      <div class="plate" role="img" aria-label="Teller mit Rosendekor" style="left:135px;top:11px;width:60px;height:60px"></div>
      <div class="tag" style="right:0;top:0;background:var(--navy)"><svg><use href="#bag"/></svg></div>
    </div>
    <div class="card pcard" style="left:11px;top:465px;width:213px;height:85px">
      <div class="name" style="left:12px;top:11px">Kuchenteller<br>altes Modell</div>
      <div class="meta" style="left:12px;top:38px">Lindhorst &amp; Sohn Heckenrose</div>
      <div class="price" style="left:12px;top:57px">€ 4,57</div>
      <div class="plate" role="img" aria-label="Teller mit Rosendekor" style="left:135px;top:11px;width:60px;height:60px"></div>
      <div class="tag" style="right:0;top:0;background:var(--navy)"><svg><use href="#bag"/></svg></div>
    </div>
    <div class="link" style="left:94px;top:557px">Mehr anzeigen</div>
    <div class="abs" style="left:0;top:601px;width:235px;height:168px;background:var(--navy)"></div>
    <div class="abs serif" style="left:21px;top:627px;font-size:10.5px;color:#fff;line-height:1.3">Wir kaufen Ihr altes Porzellan,<br>Glaswaren und Besteck</div>
    <div class="abs" style="left:21px;top:663px;width:195px;font-size:6.5px;line-height:1.55;color:#b5c2da">Zu viele Tassen im Schrank oder zu viele Teller im Keller? Gerne nimmt unser Porzellan Ankauf Ihr unverbindliches Verkaufsangebot online entgegen.</div>
    <div class="btn navy" style="left:21px;top:710px;width:193px;height:25px">Jetzt verkaufen</div>
    <div class="h2" style="left:16px;top:805px">Highlights</div>
    <div class="card" style="left:0;top:840px;width:52px;height:60px"></div>
    <div class="card" style="left:60px;top:840px;width:116px;height:60px"><div class="tag" style="left:0;top:0;border-radius:0 0 6px 0;background:var(--orange)"><svg><use href="#bag"/></svg></div></div>
    <div class="card" style="left:183px;top:840px;width:60px;height:60px"><div class="tag" style="left:0;top:0;border-radius:0 0 6px 0;background:var(--navy)"><svg><use href="#bag"/></svg></div></div>
  </div>

  <!-- Startseite Fortsetzung 1 -->
  <div class="screen" style="left:390px;top:0;width:235px;height:995px">
    <div class="h2" style="left:16px;top:22px">Highlights</div>
    <div class="card pcard" style="left:-10px;top:58px;width:63px;height:186px">
      <div class="name" style="left:6px;top:120px">r altes</div>
      <div class="meta" style="left:0;top:146px">ckenrose</div>
    </div>
    <div class="card pcard" style="left:60px;top:58px;width:116px;height:186px">
      <div class="plate" role="img" aria-label="Teller mit Rosendekor" style="left:14px;top:26px;width:88px;height:88px"></div>
      <div class="tag" style="left:0;top:0;border-radius:0 0 6px 0;background:var(--orange)"><svg><use href="#bag"/></svg></div>
      <div class="name" style="left:8px;top:121px;font-size:8.5px">Kuchenteller altes<br>Modell</div>
      <div class="meta" style="left:8px;top:146px">Lindhorst &amp; Sohn Heckenrose</div>
      <div class="price" style="left:8px;top:160px">€ 4,57</div>
    </div>
    <div class="card pcard" style="left:183px;top:58px;width:70px;height:186px">
      <div class="tag" style="left:0;top:0;border-radius:0 0 6px 0;background:var(--navy)"><svg><use href="#bag"/></svg></div>
      <div class="name" style="left:8px;top:121px;font-size:8.5px">Kuchente<br>Modell</div>
      <div class="meta" style="left:8px;top:146px">Lindhorst &amp;</div>
      <div class="price" style="left:8px;top:160px">€ 4,57</div>
    </div>
    <div class="h2" style="left:16px;top:282px">Kategorien</div>
    <div class="cat" style="top:320px"><svg><use href="#cup"/></svg>Tassen und Untertassen</div>
    <div class="cat" style="top:357px"><svg><use href="#cup"/></svg>Teller</div>
    <div class="cat" style="top:393px"><svg><use href="#cup"/></svg>Kannen &amp; Kännchen</div>
    <div class="cat" style="top:430px"><svg><use href="#cup"/></svg>Glaswaren</div>
    <div class="cat" style="top:466px"><svg><use href="#cup"/></svg>Besteck</div>
    <div class="cat" style="top:503px"><svg><use href="#cup"/></svg>Alle Kategorien</div>
    <div class="h2" style="left:17px;top:573px">Produkt des<br>Monats</div>
    <div class="img" role="img" aria-label="Weiße Untertasse mit blauem Blumendekor" style="left:0;top:630px;width:235px;height:150px;background:var(--img-bowl)"></div>
    <div class="glass" style="left:8px;top:768px;width:219px;height:197px"></div>
    <div class="abs serif" style="left:20px;top:779px;font-size:14px;line-height:1.25">Untertasse für Mokka<br>Espresso Modell 214 C</div>
    <div class="abs" style="left:20px;top:817px;font-size:8.5px;font-weight:700">Berg &amp; Grönvik I.Wahl Regentin</div>
    <div class="abs" style="left:20px;top:845px;font-size:6px">Zustand wählen:</div>
    <div class="cond" style="left:20px;top:859px"><span>1 -wie neu</span><span class="on">2 - sehr gut</span><span>3a - gut</span></div>
    <div class="abs" style="left:20px;top:889px;font-size:6px;line-height:1.4">Was bedeutet dieser Zustand?<br>• guter Zustand<br>• wenig benutzt</div>
    <div class="abs" style="left:166px;top:889px;font-size:5px">3 Stück verfügbar</div>
    <div class="abs" style="left:150px;top:895px;font-size:22px;font-weight:500">€ 4,57</div>
    <div class="link" style="left:20px;top:933px;font-size:6px">Übersicht Zustände</div>
    <svg class="abs" style="left:97px;top:930px" width="14" height="13"><use href="#heart"/></svg>
    <div class="btn" style="left:119px;top:926px;width:96px;height:24px">Zum Warenkorb</div>
    <div class="h2" style="left:16px;top:985px">Herstell</div>
  </div>

  <!-- Startseite Fortsetzung 2 -->
  <div class="screen" style="left:675px;top:0;width:235px;height:995px">
    <div class="glass" style="left:5px;top:-10px;width:225px;height:60px"></div>
    <div class="abs" style="left:30px;top:-2px;font-size:5.5px;line-height:1.3">• guter Zustand<br>• wenig benutzt</div>
    <div class="abs" style="left:152px;top:-6px;font-size:19px;font-weight:500">€ 4,57</div>
    <div class="link" style="left:20px;top:31px;font-size:6px">Übersicht Zustände</div>
    <svg class="abs" style="left:97px;top:28px" width="14" height="13"><use href="#heart"/></svg>
    <div class="btn" style="left:119px;top:24px;width:96px;height:24px">Zum Warenkorb</div>
    <div class="h2" style="left:16px;top:91px">Hersteller</div>
    <div class="chips" style="left:16px;top:124px;width:210px">
      <span class="chip">Weißenau</span><span class="chip">Royal Ashby</span><span class="chip">Lindhorst &amp; Sohn</span>
      <span class="chip">Eschental</span><span class="chip">Nachtfeld</span><span class="chip">Rosenau</span>
      <span class="chip">Royal Nordhavn</span><span class="chip">Marcelli</span><span class="chip">Tomberg</span>
    </div>
    <div class="link" style="left:93px;top:199px">Mehr anzeigen</div>
    <div class="img" role="img" aria-label="Hände verpacken Geschirr in Packpapier" style="left:0;top:241px;width:235px;height:161px;background:var(--img-paper)"></div>
    <div class="h2" style="left:16px;top:423px">Profis im Verpacken</div>
    <div class="para" style="left:16px;top:452px;width:205px;font-size:7.5px">Wir haben jahrelange Erfahrung im Verpacken von Porzellan und Glaswaren und vielen anderen zerbrechlichen Gegenständen und verwenden zum Verpacken nur hochwertige Materialien, um sicherzustellen, dass jedes einzelne Produkt sicher den Weg zu unseren Kunden findet.</div>
    <div class="btn outline" style="left:16px;top:541px;width:68px;height:24px">mehr erfahren</div>
    <div class="img" role="img" aria-label="Viele blau-weiße Teller auf einem Tisch" style="left:0;top:606px;width:235px;height:161px;background:var(--img-plates)"></div>
    <div class="h2" style="left:16px;top:788px">Gebraucht statt neu</div>
    <div class="para" style="left:16px;top:817px;width:205px;font-size:7.5px">Durch den Kauf von gebrauchten Produkten tragen Sie dazu bei, den Verbrauch von neuen Rohstoffen und die Umweltverschmutzung zu reduzieren, die bei der Herstellung von neuen Produkten entstehen. Im Sinne einer Circular Economy werden Produkte in einen andauernden Nutzungskreislauf von Person zu Person weitergegeben, wodurch alle Beteiligten profitieren und ganz nebenbei unsere Umwelt geschont wird.</div>
    <div class="btn outline" style="left:16px;top:956px;width:68px;height:24px">mehr erfahren</div>
  </div>

  <!-- Footer-Menü -->
  <div class="screen" style="left:960px;top:0;width:235px;height:376px;background:var(--navy);border-radius:0 0 14px 14px">
    <div class="foot" style="top:13px">AGB</div>
    <div class="foot" style="top:38px">Cookie-Einstellungen</div>
    <div class="foot serif" style="top:88px;font-size:14px;color:#b5c2da">Rechtliches</div>
    <div class="foot" style="top:114px">Abgabemöglichkeiten</div>
    <div class="foot" style="top:139px">FAQ</div>
    <div class="foot" style="top:164px">FAQ - Ankauf</div>
    <div class="foot" style="top:190px">Kontakt</div>
    <div class="foot" style="top:215px">Qualitätsstufen der Artikel</div>
    <div class="foot" style="top:240px">Richtlinien zum Ankauf</div>
    <div class="foot" style="top:265px">Verpackungsanleitungen</div>
    <div class="foot" style="top:290px">Versandkosten</div>
    <div class="foot" style="top:315px">Verpackungmaterialstore</div>
  </div>

  <!-- Hersteller -->
  <div class="screen" style="left:960px;top:412px;width:235px;height:510px;border-radius:14px">
    <div class="img" role="img" aria-label="Bunt bemaltes Porzellan mit Blumenmotiv" style="left:0;top:0;width:235px;height:193px;background:linear-gradient(135deg,#cfd4c3 0%,#d98f4a 45%,#6a7f5e 100%)"></div>
    <div class="logo"><i></i>Tassenfund</div><div class="burger"></div>
    <div class="glass" style="left:10px;top:93px;width:217px;height:99px"></div>
    <div class="abs serif" style="left:26px;top:106px;font-size:19px;white-space:nowrap">Lindhorst &amp; Sohn</div>
    <div class="btn" style="left:26px;top:148px;width:122px;height:24px">Mehr über den Hersteller</div>
    <div class="h2" style="left:16px;top:210px">Beliebte Serien</div>
    <div class="card" style="left:-10px;top:240px;width:58px;height:136px"><div class="abs" style="left:12px;top:117px;font-size:7px;font-weight:700">ca</div></div>
    <div class="card" style="left:55px;top:240px;width:118px;height:136px">
      <div class="plate" role="img" aria-label="Teller mit Rosendekor" style="left:15px;top:14px;width:88px;height:88px"></div>
      <div class="abs serif" style="left:0;width:118px;text-align:center;top:117px;font-size:8px">Heckenrose</div>
    </div>
    <div class="card" style="left:180px;top:240px;width:60px;height:136px">
      <div class="img" role="img" aria-label="Weißer Teller mit Reliefmuster" style="left:15px;top:22px;width:60px;height:70px;border-radius:50%;background:#d9e0ea"></div>
      <div class="abs" style="left:46px;top:117px;font-size:7px;font-weight:700">G</div>
    </div>
    <div class="h2" style="left:16px;top:398px">Produktkategorien</div>
    <div class="chips" style="left:16px;top:430px;width:210px">
      <span class="chip">Besteck</span><span class="chip">Tassen &amp; Untertassen</span><span class="chip">Teller</span>
      <span class="chip">Vasen</span><span class="chip">Glaswaren</span><span class="chip">Platten und Schüsseln</span>
      <span class="chip">Kannen &amp; Kännchen</span><span class="chip out">Alle Kategorien</span>
    </div>
  </div>
  <div class="label" style="left:1077px;top:947px">Hersteller</div>

  <!-- Collection -->
  <div class="screen" style="left:1245px;top:412px;width:236px;height:510px;border-radius:14px">
    <div class="logo"><i></i>Tassenfund</div><div class="burger"></div>
    <div class="h2" style="left:12px;top:54px;font-size:19px">Lindhorst &amp; Sohn<br>Heckenrose</div>
    <div class="abs serif" style="left:12px;top:108px;font-size:10px">Highlights</div>
    <div class="card pcard" style="left:-10px;top:130px;width:63px;height:186px">
      <div class="name" style="left:6px;top:121px;font-size:8.5px">r altes</div>
      <div class="meta" style="left:0;top:147px">ckenrose</div>
    </div>
    <div class="card pcard" style="left:60px;top:130px;width:116px;height:186px">
      <div class="plate" role="img" aria-label="Teller mit Rosendekor" style="left:14px;top:26px;width:88px;height:88px"></div>
      <div class="tag" style="left:0;top:0;border-radius:0 0 6px 0;background:var(--orange)"><svg><use href="#bag"/></svg></div>
      <div class="name" style="left:8px;top:122px;font-size:8.5px">Kuchenteller altes<br>Modell</div>
      <div class="meta" style="left:8px;top:147px">Lindhorst &amp; Sohn Heckenrose</div>
      <div class="price" style="left:8px;top:161px">€ 4,57</div>
    </div>
    <div class="card pcard" style="left:183px;top:130px;width:70px;height:186px">
      <div class="tag" style="left:0;top:0;border-radius:0 0 6px 0;background:var(--navy)"><svg><use href="#bag"/></svg></div>
      <div class="name" style="left:8px;top:122px;font-size:8.5px">Kuchente<br>Modell</div>
      <div class="meta" style="left:8px;top:147px">Lindhorst &amp;</div>
      <div class="price" style="left:8px;top:161px">€ 4,57</div>
    </div>
    <div class="abs serif" style="left:12px;top:335px;font-size:10px">Collection</div>
    <div class="card pcard" style="left:10px;top:356px;width:213px;height:80px">
      <div class="name" style="left:12px;top:11px">Kuchenteller<br>altes Modell</div>
      <div class="meta" style="left:12px;top:38px">Lindhorst &amp; Sohn Heckenrose</div>
      <div class="price" style="left:12px;top:56px">€ 4,57</div>
      <div class="img" role="img" aria-label="Tasse mit Untertasse und Rosendekor" style="left:130px;top:22px;width:68px;height:38px;border-radius:50%;background:var(--img-plate)"></div>
      <div class="tag" style="right:0;top:0;background:var(--navy)"><svg><use href="#bag"/></svg></div>
    </div>
    <div class="card pcard" style="left:10px;top:450px;width:213px;height:80px">
      <div class="name" style="left:12px;top:11px">Kuchenteller<br>altes Modell</div>
      <div class="meta" style="left:12px;top:38px">Lindhorst &amp; Sohn Heckenrose</div>
      <div class="plate" role="img" aria-label="Teller mit Rosendekor" style="left:138px;top:12px;width:56px;height:56px"></div>
      <div class="tag" style="right:0;top:0;background:var(--navy)"><svg><use href="#bag"/></svg></div>
    </div>
  </div>
  <div class="label" style="left:1362px;top:947px">Collection</div>

  <!-- Produktdetailseite -->
  <div class="screen" style="left:1532px;top:412px;width:235px;height:510px;border-radius:14px">
    <div class="logo"><i></i>Tassenfund</div><div class="burger"></div>
    <div class="img" role="img" aria-label="Weiße Untertasse mit blauem Blumendekor" style="left:0;top:48px;width:235px;height:262px;background:var(--img-bowl)"></div>
    <div class="abs" style="left:217px;top:57px;display:flex;flex-direction:column;gap:4px">
      <i style="width:4px;height:4px;border-radius:50%;border:1px solid var(--navy)"></i>
      <i style="width:4px;height:4px;border-radius:50%;background:var(--navy)"></i>
      <i style="width:4px;height:4px;border-radius:50%;border:1px solid var(--navy)"></i>
      <i style="width:4px;height:4px;border-radius:50%;border:1px solid var(--navy)"></i>
    </div>
    <div class="glass" style="left:8px;top:306px;width:222px;height:204px"></div>
    <div class="abs serif" style="left:20px;top:317px;font-size:14px;line-height:1.25">Untertasse für Mokka<br>Espresso Modell 214 C</div>
    <div class="abs" style="left:20px;top:356px;font-size:8.5px;font-weight:700">Berg &amp; Grönvik I.Wahl Regentin</div>
    <div class="abs" style="left:20px;top:384px;font-size:6px">Zustand wählen:</div>
    <div class="cond" style="left:20px;top:398px"><span>1 -wie neu</span><span class="on">2 - sehr gut</span><span>3a - gut</span><span>3b - gut</span></div>
    <div class="abs" style="left:20px;top:428px;font-size:6px;line-height:1.4">Was bedeutet dieser Zustand?<br>• guter Zustand<br>• wenig benutzt</div>
    <div class="abs" style="left:165px;top:428px;font-size:5px">3 Stück verfügbar</div>
    <div class="abs" style="left:151px;top:434px;font-size:22px;font-weight:500">€ 4,57</div>
    <div class="link" style="left:20px;top:472px;font-size:6px">Übersicht Zustände</div>
    <svg class="abs" style="left:97px;top:469px" width="14" height="13"><use href="#heart"/></svg>
    <div class="btn" style="left:119px;top:465px;width:96px;height:24px">Zum Warenkorb</div>
  </div>
  <div class="label" style="left:1650px;top:944px">Produktdetailseite</div>

</div>
</div>
</body>
</html>
```